Marketing Poster for Addiction Recovery Facility

We are looking for a unique marketing poster (8.5x11). We would like the poster to describe our services, and position us the industry leader in the addiction recovery health care space. - I've attached some examples as to what I would like the flyer to look like as well as attached a document listing our services and credentials.

Birchwell Healing House of Middle Tennessee
Our Phone number is 615-555-0147
Our Fax number is 615-555-0192
Physical Address - 4817 West Larkspur Hollow Rd
Mount Juliet, TN 37122
Our web address is www.birchwellhealing.example

Target Market(s)

Addiction Recovery Patients

Industry/Entity Type

Mental Health

Font styles to use
Other font styles liked:
• I'm open to the font choice, but it should be similar to the posters attached.

Colors

Designer to choose colors to be used in the design.

Requirements
Must have
• Look similar to the poster examples attached.
Nice to have
• Follow our Birchwell Healing Color Scheme
Should not have
• We are open to ideas, but it should look similar to the posters attached.

```html
<!DOCTYPE html>
<html lang="en">
<head>
<meta charset="utf-8">
<title>Birchwell Healing House of Middle Tennessee</title>
<link rel="stylesheet" href="https://fonts.googleapis.com/css2?family=Alfa+Slab+One&family=Enriqueta:wght@400;600&family=Open+Sans:wght@600;700&family=Roboto+Condensed:wght@800&display=swap">
<style>
  :root {
    --ink: #141a22;
    --cream: #f8f3d2;
    --sky: #7d93cf;
    --sun: #f6efc9;
    --service-blue: #2b6cc3;
    --white: #ffffff;
  }
  * { margin: 0; padding: 0; box-sizing: border-box; }
  html, body { width: 912px; height: 1200px; overflow: hidden; background: var(--ink); }
  .poster {
    position: relative;
    width: 912px;
    height: 1200px;
    background: var(--ink);
  }
  .sheet {
    position: absolute;
    left: 27px; top: 27px;
    width: 859px; height: 1146px;
    background: var(--cream);
  }
  .rule {
    position: absolute;
    left: 41px; width: 777px;
    height: 5px;
    background: var(--ink);
  }
  .rule--top { top: 20px; }
  .rule--bottom { top: 1118px; }
  .hero {
    position: absolute;
    left: 43px; top: 35px;
    width: 773px; height: 613px;
    background:
      radial-gradient(circle at 73% 42%, var(--sun) 0 29%, transparent 29.3%),
      linear-gradient(to bottom, var(--sky) 0 45%, var(--ink) 45% 100%);
  }
  .hero__figure {
    position: absolute;
    left: 355px; top: 280px;
    width: 418px; height: 333px;
    background: linear-gradient(135deg, var(--sky), #5a6f9f 60%, var(--ink));
    opacity: 0.85;
  }
  .title {
    position: absolute;
    left: 64px; top: 72px;
    font-family: "Alfa Slab One", Georgia, serif;
    font-size: 50px;
    line-height: 60px;
    letter-spacing: 2px;
    color: var(--ink);
    text-transform: uppercase;
  }
  .credentials {
    position: absolute;
    left: 43px; top: 362px;
    width: 377px; height: 158px;
    background: var(--ink);
    color: var(--cream);
    font-family: "Enriqueta", Georgia, serif;
    font-size: 17px;
    line-height: 22px;
    text-align: center;
    padding-top: 19px;
    letter-spacing: 0.3px;
  }
  .section-heading {
    position: absolute;
    left: 43px; top: 688px;
    width: 773px;
    display: flex;
    align-items: center;
    gap: 16px;
    font-family: "Open Sans", Arial, sans-serif;
    font-weight: 700;
    font-size: 39px;
    color: var(--ink);
    letter-spacing: 0.5px;
  }
  .section-heading::before,
  .section-heading::after {
    content: "";
    flex: 1;
    height: 9px;
    background: var(--ink);
  }
  .section-heading::before { flex: 0 0 100px; }
  .section-heading::after { flex: 0 0 100px; }
  .services {
    font-family: "Enriqueta", Georgia, serif;
    font-weight: 600;
    font-size: 26px;
    color: var(--service-blue);
    letter-spacing: 0.6px;
  }
  .services span { position: absolute; white-space: nowrap; }
  .contact-band {
    position: absolute;
    left: 43px; top: 891px;
    width: 773px; height: 128px;
    background: var(--ink);
    color: var(--white);
    font-family: "Roboto Condensed", Arial Narrow, sans-serif;
    font-weight: 800;
    font-size: 45px;
    line-height: 54px;
    text-align: center;
    padding-top: 10px;
  }
  .address {
    position: absolute;
    left: 0; top: 1026px;
    width: 859px;
    text-align: center;
    font-family: "Open Sans", Arial, sans-serif;
    font-weight: 700;
    font-size: 17.5px;
    line-height: 29px;
    color: var(--ink);
  }
  .corner-mark {
    position: absolute;
    top: 1068px;
    width: 56px; height: 40px;
  }
  .corner-mark--left { left: 50px; }
  .corner-mark--right { left: 753px; }
</style>
</head>
<body>
<main class="poster">
  <div class="sheet">
    <div class="rule rule--top"></div>

    <div class="hero" role="img" aria-label="Illustration of three cedar trees silhouetted against a pale sun in a blue sky, above the silhouette of a person sitting with head bowed">
      <div class="hero__figure"></div>
    </div>

    <h1 class="title">Birchwell Healing<br>House of<br>Middle<br>Tennessee</h1>

    <section class="credentials">
      <div>CREDENTIALS</div>
      <div>Licensed Office Based Opiate</div>
      <div>Treatment Facility</div>
      <div>Licensed Professional Counselors</div>
      <div>Board Certified Addictionologist</div>
    </section>

    <h2 class="section-heading">TREATMENT SERVICES</h2>

    <div class="services">
      <span style="left:112px; top:730px;">Medication Assisted Opioid Treatment</span>
      <span style="left:63px; top:764px;">Individual Counseling</span>
      <span style="left:63px; top:800px;">Family Counseling Services</span>
      <span style="left:63px; top:836px;">Sex Addiction</span>
      <span style="left:500px; top:764px;">Gambling Addiction</span>
      <span style="left:500px; top:800px;">Sex Addiction</span>
      <span style="left:500px; top:836px;">Aftercare Program</span>
    </div>

    <section class="contact-band">
      <div>Phone number 615-555-0147</div>
      <div>Fax number 615-555-0192</div>
    </section>

    <address class="address" style="font-style:normal;">
      <div>Physical Address - 4817 West Larkspur Hollow Rd</div>
      <div>Mount Juliet, TN 37122</div>
      <div>Website:&nbsp; www.birchwellhealing.example</div>
    </address>

    <div class="corner-mark corner-mark--left" role="img" aria-label="Small leaf corner flourish"><svg width="56" height="40"><rect x="4" y="6" width="48" height="28" rx="6" fill="#141a22"/></svg></div>
    <div class="corner-mark corner-mark--right" role="img" aria-label="Small leaf corner flourish"><svg width="56" height="40"><rect x="4" y="6" width="48" height="28" rx="6" fill="#141a22"/></svg></div>

    <div class="rule rule--bottom"></div>
  </div>
</main>
</body>
</html>
```